Indoor location business needs re-design two websites (one website and one back office)

We are a company active in the indoor location and navigation industry. We are developing software and SDKs.
We are looking for someone who will re-design two of our websites.
Color and style have to become similar and the design as to be improved.
The first:
https://indoor.brackelvane.com
You will find all the content attached
The second
https://indoor.brackelvane.com/indoor/admin/
Here are credentials for this one.
Account: design
password: plover847
You will find directly the content on the page.
Target Market(s)
hospital, airport, event organization, retail, museum
Industry/Entity Type
Business
Number of Pages Required
5+ page
Requirements
Must have
- The contain that are on each page of both websites.

```html
<!DOCTYPE html>
<html lang="en">
<head>
<meta charset="utf-8">
<title>Use Cases – Brackelvane Indoor</title>
<link href="https://fonts.googleapis.com/css2?family=Open+Sans:wght@400;600;700&display=swap" rel="stylesheet">
<style>
:root{
  --cyan:#12b5ea;
  --cyan-dark:#0d9cc9;
  --ink:#3b3b3b;
  --text:#7a7a7a;
  --light:#f1f1f1;
  --rule:#e2e2e2;
  --nav:#4a4a4a;
  --footer:#3a3a3a;
  --footer-bottom:#2e2e2e;
  --white:#ffffff;
}
*{box-sizing:border-box;margin:0;padding:0}
html,body{width:1200px;height:3436px;overflow:hidden}
body{font-family:"Open Sans",Arial,sans-serif;color:var(--text);font-size:12px;line-height:1.6;background:var(--white)}
.wrap{width:780px;margin:0 auto}
/* header */
.site-header{height:100px;background:var(--white);position:relative}
.social-row{position:absolute;left:220px;top:12px;display:flex;gap:4px}
.social-row span{width:14px;height:14px;background:var(--cyan);display:block}
.brand{position:absolute;left:220px;top:34px;display:flex;align-items:center;gap:8px}
.brand-mark{width:40px;height:40px;background:var(--cyan)}
.brand-name{font-size:17px;font-weight:700;color:var(--cyan)}
.search{position:absolute;left:440px;top:56px;width:230px;height:24px;border:1px solid var(--rule);font-size:11px;color:#aaa;padding:3px 8px}
.auth{position:absolute;right:240px;top:56px;display:flex;gap:8px}
.auth span{height:24px;padding:0 16px;font-size:10px;line-height:24px;color:var(--white);background:#bdbdbd}
.auth .signup{background:var(--cyan)}
.main-nav{height:28px;background:var(--nav);display:flex;justify-content:center}
.main-nav a{color:#e6e6e6;text-decoration:none;font-size:10px;font-weight:600;line-height:28px;padding:0 22px;text-transform:uppercase}
.main-nav a.active{background:var(--cyan);color:var(--white)}
/* hero */
.hero{height:252px;background:var(--cyan);text-align:center;color:var(--white);padding-top:30px}
.hero h1{display:inline-block;border:2px solid var(--white);font-size:26px;font-weight:700;padding:4px 18px;letter-spacing:1px}
.hero h1 b{font-weight:400}
.hero p{font-size:18px;margin-top:12px}
.hero-links{display:flex;justify-content:center;gap:20px;margin-top:30px}
.hero-links a{width:116px;height:56px;border:1px solid var(--white);color:var(--white);text-decoration:none;font-size:12px;display:flex;align-items:center;justify-content:center;text-align:center;line-height:1.3}
/* sections */
.case{padding-top:40px;overflow:hidden}
.case.alt{background:var(--light)}
.case-event{height:440px}
.case-retail{height:680px}
.case-hospital,.case-airports,.case-museum{height:520px}
.case h2{text-align:center;font-size:22px;font-weight:700;color:var(--ink);letter-spacing:1px}
.case h2 em{font-style:normal;color:var(--cyan)}
.case h2::after{content:"";display:block;width:120px;height:2px;background:var(--cyan);margin:6px auto 0}
.case-body{display:flex;gap:40px;margin-top:36px}
.case-intro{width:350px}
.case-intro p{margin-bottom:12px}
.case-intro ul{list-style:none;margin-top:8px}
.case-intro li{color:var(--cyan);padding-left:12px;position:relative;margin-bottom:2px}
.case-intro li::before{content:"";position:absolute;left:0;top:8px;width:4px;height:4px;background:var(--cyan)}
.case-points{width:390px}
.case-points h3{color:var(--cyan);font-size:12px;font-weight:700;text-transform:uppercase;margin-top:14px}
.case-points h3:first-child{margin-top:0}
.case-points p{margin-top:2px}
/* footer */
.site-footer{height:290px;background:var(--footer);color:#bdbdbd;padding-top:40px}
.footer-cols{width:780px;margin:0 auto;display:flex;gap:40px;position:relative}
.footer-cols h4{color:var(--white);font-size:11px;text-transform:uppercase;margin-bottom:10px;border-bottom:1px solid #555;padding-bottom:4px}
.col-sitemap{width:160px}
.col-sitemap ul{list-style:none;columns:2;font-size:11px;line-height:2.1}
.col-news{width:230px;font-size:10px;line-height:1.5}
.col-news p{margin-bottom:10px}
.col-news b{color:#e0e0e0}
.col-contact{width:180px;font-size:11px;line-height:2.2}
.col-contact .icons{display:flex;gap:4px;margin:4px 0}
.col-contact .icons span{width:14px;height:14px;background:var(--cyan)}
.footer-brand{position:absolute;right:0;top:10px;display:flex;align-items:center;gap:8px}
.footer-brand .mark{width:70px;height:70px;background:#555}
.footer-brand .name{color:var(--white);font-size:15px;font-weight:700}
.footer-bottom{height:86px;background:var(--footer-bottom);text-align:center;font-size:10px;color:#8a8a8a;line-height:86px}
</style>
</head>
<body>
<header class="site-header">
  <div class="social-row"><span></span><span></span><span></span><span></span><span></span></div>
  <div class="brand"><span class="brand-mark"></span><span class="brand-name">brackelvane</span></div>
  <div class="search">Search…</div>
  <div class="auth"><span>LOGIN</span><span class="signup">SIGN UP</span></div>
</header>
<nav class="main-nav">
  <a href="#">Home</a><a href="#" class="active">Use cases</a><a href="#">Price</a><a href="#">Free trial</a><a href="#">Developer</a><a href="#">FAQ</a><a href="#">About</a><a href="#">Contact</a><a href="#">Login</a>
</nav>

<section class="hero">
  <h1>USE <b>CASES</b></h1>
  <p>Industries which trust our technology</p>
  <div class="hero-links">
    <a href="#event">Event Organization</a><a href="#retail">Retail</a><a href="#hospital">Hospital</a><a href="#airports">Airports</a><a href="#museum">Museum</a>
  </div>
</section>

<section class="case case-event" id="event">
  <h2><em>EVENT</em> ORGANIZATION</h2>
  <div class="wrap case-body">
    <div class="case-intro">
      <p>Trade fairs and large events bring thousands of visitors into unfamiliar halls. Our indoor maps guide every guest to the right stand, room or service in seconds, directly from a smartphone.</p>
      <p>Organisers gain a clear view of visitor flows and can adapt the venue in real time.</p>
      <ul><li>An interactive floor plan</li><li>Navigation</li><li>Analytics of visitor flows</li><li>Location</li></ul>
    </div>
    <div class="case-points">
      <h3>Help exhibitors adjust stand placement</h3>
      <p>Heat maps show where visitors stop and which aisles stay empty, so space can be sold and arranged better.</p>
      <h3>Navigation</h3>
      <p>Guests find stands, talks and exits with turn-by-turn directions inside every hall.</p>
      <h3>Boost the experience</h3>
      <p>Push schedules and reminders based on the visitor's position in the venue.</p>
      <h3>Statistics</h3>
      <p>Measure attendance per zone and per hour to plan the next edition with confidence.</p>
    </div>
  </div>
</section>

<section class="case alt case-retail" id="retail">
  <h2>RETAIL</h2>
  <div class="wrap case-body">
    <div class="case-intro">
      <p>Shopping centres and large stores use indoor location to connect the physical shop with the digital world. Shoppers find products quickly and receive relevant offers at the right shelf.</p>
      <p>Our SDK integrates easily into existing retail apps and loyalty programmes.</p>
      <ul><li>Product search on the map</li><li>Location-based promotions</li><li>Customer journey analytics</li><li>Click and collect guidance</li></ul>
    </div>
    <div class="case-points">
      <h3>Improve the shopping time</h3>
      <p>Customers locate products, departments and cashiers without searching, saving time and reducing frustration during every visit.</p>
      <h3>Create a new sales channel</h3>
      <p>Send targeted offers when a shopper walks near a promoted item and turn passing traffic into purchases.</p>
      <p>Partners and brands can rent digital visibility on the map, creating new income for the store.</p>
      <h3>Increase customer satisfaction and loyalty</h3>
      <p>Give loyal customers a personal shopping assistant that remembers preferences, lists and favourite stores, and guides them through the centre.</p>
      <p>A smooth visit makes customers come back more often and spend more time in the shop.</p>
      <h3>Data collection</h3>
      <p>Collect anonymous data on paths, dwell time and peak hours. Use it to optimise layouts, staffing and merchandising.</p>
      <p>Compare zones, measure the effect of campaigns and follow trends over weeks and months.</p>
    </div>
  </div>
</section>

<section class="case case-hospital" id="hospital">
  <h2>HOSPITAL</h2>
  <div class="wrap case-body">
    <div class="case-intro">
      <p>Hospitals are complex buildings where patients and visitors often get lost. Indoor navigation reduces stress and late arrivals, and frees staff from giving directions all day long.</p>
      <p>Medical teams also benefit from locating equipment and colleagues quickly.</p>
      <ul><li>Patient guidance</li><li>Asset tracking</li><li>Staff location</li></ul>
    </div>
    <div class="case-points">
      <h3>Guide management</h3>
      <p>Patients receive directions to the right department as soon as they enter the building.</p>
      <p>Appointments start on time because nobody wanders through the corridors.</p>
      <h3>Welcome people and guarantee service</h3>
      <p>Visitors find rooms, cafeterias and parking in a few taps, even at night.</p>
      <p>Reception desks spend more time on care and less on orientation.</p>
      <h3>Equipment location</h3>
      <p>Find wheelchairs, pumps and mobile devices instantly on the map.</p>
      <p>Reduce losses and purchase costs by knowing where every asset is.</p>
    </div>
  </div>
</section>

<section class="case alt case-airports" id="airports">
  <h2><em>AIRPORTS</em></h2>
  <div class="wrap case-body">
    <div class="case-intro">
      <p>Airports handle millions of travellers who are short on time. Indoor location shows the fastest way to gates, shops and services, and keeps passengers informed.</p>
      <ul><li>Gate and service navigation</li><li>Commercial offers in the terminal</li><li>Passenger flow monitoring</li></ul>
    </div>
    <div class="case-points">
      <h3>Help the travellers to find their gate</h3>
      <p>Passengers see walking time to their gate and receive alerts when boarding starts.</p>
      <p>Fewer missed flights and calmer terminals for everyone.</p>
      <h3>Increase the shop and services revenue</h3>
      <p>Travellers with spare time are guided to shops, restaurants and lounges nearby.</p>
      <p>Offers appear when passengers are close to the store.</p>
      <h3>Better understanding the travellers</h3>
      <p>Analyse queues and flows to open counters and security lanes at the right moment.</p>
    </div>
  </div>
</section>

<section class="case case-museum" id="museum">
  <h2>MUSEUM</h2>
  <div class="wrap case-body">
    <div class="case-intro">
      <p>Museums use indoor location to offer rich, personal tours. Visitors discover works at their own pace while content appears automatically near each piece.</p>
      <ul><li>Location-based audio guides</li><li>Thematic tours</li><li>Visitor analytics</li></ul>
    </div>
    <div class="case-points">
      <h3>Content management and interactivity</h3>
      <p>Curators attach texts, audio and video to rooms and objects from the back office. Content is triggered when the visitor stands in front of the work and can be updated at any time.</p>
      <p>Games and quizzes make the visit more engaging for younger audiences.</p>
      <h3>Navigation and itineraries</h3>
      <p>Propose short or long tours, accessible routes and paths through temporary exhibitions, always with clear directions.</p>
      <h3>Better knowledge of your visitors</h3>
      <p>Learn which rooms attract the most interest and how long people stay, and plan exhibitions based on real visitor behaviour.</p>
    </div>
  </div>
</section>

<footer class="site-footer">
  <div class="footer-cols">
    <div class="col-sitemap">
      <h4>Sitemap</h4>
      <ul><li>Home</li><li>Use cases</li><li>Price</li><li>Free trial</li><li>Developer</li><li>FAQ</li><li>About</li><li>Contact</li></ul>
    </div>
    <div class="col-news">
      <h4>Recent posts</h4>
      <p><b>New indoor maps for retail</b><br>Our latest release brings faster routing and new map styles.</p>
      <p><b>Hospital pilot launched</b><br>Patients now find departments using their phones.</p>
      <p><b>SDK update available</b><br>Version 3 adds better positioning in large halls.</p>
    </div>
    <div class="col-contact">
      <h4>Contact</h4>
      <div>Corvel, Switzerland</div>
      <div>+41 21 555 01 47</div>
      <div>info@brackelvane.com</div>
      <div class="icons"><span></span><span></span><span></span><span></span></div>
    </div>
    <div class="footer-brand"><span class="mark"></span><span class="name">brackelvane</span></div>
  </div>
</footer>
<div class="footer-bottom">© 2024 brackelvane.com – All rights reserved</div>
</body>
</html>
```